Redesigning of the packaging for 4 GOLDEN HEARTH gourmet breads

We need new designs for our range of four gourmet sliced breads, called GOLDEN HEARTH. These breads are prepared with specially selected ingredients sourced from several countries and with extreme focus on quality, health and indulgent pleasure. The Golden Hearth brand aims to solve the boring and bland nature of white breads and comes in several flavours such as coconut, seeds & nuts, exotic fruits and vegetables, buttermilk, chocolate, etc.
The Golden Hearth brand positioning statement is JOY IN EVERY SLICE
The current packaging designs are still quite attractive which makes it a difficult decision, but we know it's time for a rebrand, and therefore we really want the best possible designs - ONLY THE BEST!
GOLDEN HEARTH currently comprises three 'sister' products and one new addition named as follows:
1. Golden Hearth - buttermilk dream (yellow color)
2. Golden Hearth - cocoa swirl (brown & orange color)
3. Golden Hearth - tropic coconut (green & cream color)
4. Hearth Tots - (kiddies' style - This is a kiddies bread)
[Some pictures of the current packaging are attached, alongside with the content, layout and dimensions which should be used for the new designs, including ingredients, addresses, etc. Check the file 'Back view with ingredients and contents.pdf'; 'Layout and Dimensions of current Golden Hearth Packaging.pdf]
5. The logo may or may not be modified. (Golden Hearth Logo.pdf)
Key points to note:
- Demographic: The target audience is mainly young and middle aged from the middle to upper economic class
- Psychographic: Health conscious, Class conscious, Family focused consumers, Environment and Sustainable development minded consumers
- The designs will be similar in style for the 3 variants but be differentiated by colours and content
- The fonts and the overall design should be modern, playful and inviting.
- The content of the packaging is in the attachments
- Total designs - 4 designs.
Target Market(s)
The target market is kids, teens, young adults. Middle to upper economic class. Premium segment, lifestyle conscious consumers.
Industry/Entity Type
Bakery
Colors
Designer to choose colors to be used in the design.
Look and feel

```html
<!DOCTYPE html>
<html lang="en">
<head>
<meta charset="utf-8">
<title>Golden Hearth – Buttermilk Dream Pack Range</title>
<link rel="stylesheet" href="https://fonts.googleapis.com/css2?family=Exo+2:wght@800;900&display=swap">
<style>
  :root {
    --canvas: #ffffff;
    --yellow-base: #ecc91a;
    --yellow-light: #fff28a;
    --yellow-title: #1a4fb0;
    --red-base: #7a0c0c;
    --red-light: #c8321e;
    --red-title: #f7a11a;
    --green-base: #17632f;
    --green-light: #4fae5e;
    --green-title: #f1dc55;
    --pill: #f08a12;
    --pill-text: #ffffff;
    --badge: #ffffff;
    --rim-red: #d8361a;
    --rim-orange: #f39a1e;
    --loaf-light: #d8b79a;
    --loaf-dark: #8e6448;
  }
  html, body {
    margin: 0;
    padding: 0;
    width: 1127px;
    height: 1200px;
    overflow: hidden;
    background: var(--canvas);
  }
  .pack-range { display: block; width: 1127px; height: 1200px; }
  .pack-title {
    font-family: "Exo 2", sans-serif;
    font-weight: 900;
    font-size: 64px;
    letter-spacing: -1px;
  }
  .pack--yellow .pack-title { fill: var(--yellow-title); }
  .pack--red .pack-title { fill: var(--red-title); }
  .pack--green .pack-title { fill: var(--green-title); }
  .flavour-pill { fill: var(--pill); }
  .flavour-label {
    font-family: "Exo 2", sans-serif;
    font-weight: 800;
    font-size: 17px;
    fill: var(--pill-text);
    letter-spacing: 0.5px;
  }
  .quality-badge { fill: var(--badge); opacity: 0.92; }
  .sun-rays { fill: #ffffff; opacity: 0.16; }
  .bread-window { stroke-width: 7; }
  .pack--yellow .bread-window { stroke: var(--rim-red); }
  .pack--red .bread-window,
  .pack--green .bread-window { stroke: var(--rim-orange); }
</style>
</head>
<body>
<svg class="pack-range" viewBox="0 0 1127 1200" xmlns="http://www.w3.org/2000/svg">
  <defs>
    <path id="bag-outline" d="M25,8 C250,0 500,14 690,6 C715,60 730,100 742,118 C790,80 840,40 880,20 L872,140 L884,262 C840,240 790,200 742,160 C730,190 712,230 690,268 C480,276 240,264 25,272 Q0,272 0,245 L0,35 Q0,8 25,8 Z"/>
    <clipPath id="bag-clip"><use href="#bag-outline"/></clipPath>
    <path id="bread-heart" d="M325,270 L325,200 C325,140 360,105 410,108 C440,110 455,125 465,135 C485,70 540,45 600,50 C660,55 690,95 690,140 L690,266 Z"/>
    <path id="ray" d="M0,0 L1000,-45 L1000,45 Z"/>
    <g id="sunburst" class="sun-rays">
      <use href="#ray" transform="rotate(0)"/>
      <use href="#ray" transform="rotate(20)"/>
      <use href="#ray" transform="rotate(40)"/>
      <use href="#ray" transform="rotate(60)"/>
      <use href="#ray" transform="rotate(80)"/>
      <use href="#ray" transform="rotate(100)"/>
      <use href="#ray" transform="rotate(120)"/>
      <use href="#ray" transform="rotate(140)"/>
      <use href="#ray" transform="rotate(160)"/>
      <use href="#ray" transform="rotate(180)"/>
      <use href="#ray" transform="rotate(200)"/>
      <use href="#ray" transform="rotate(220)"/>
      <use href="#ray" transform="rotate(240)"/>
      <use href="#ray" transform="rotate(260)"/>
      <use href="#ray" transform="rotate(280)"/>
      <use href="#ray" transform="rotate(300)"/>
      <use href="#ray" transform="rotate(320)"/>
      <use href="#ray" transform="rotate(340)"/>
    </g>
    <radialGradient id="glow-yellow" cx="0.2" cy="0.5" r="0.9">
      <stop offset="0" stop-color="var(--yellow-light)"/>
      <stop offset="1" stop-color="var(--yellow-base)"/>
    </radialGradient>
    <radialGradient id="glow-red" cx="0.2" cy="0.5" r="0.9">
      <stop offset="0" stop-color="var(--red-light)"/>
      <stop offset="1" stop-color="var(--red-base)"/>
    </radialGradient>
    <radialGradient id="glow-green" cx="0.2" cy="0.5" r="0.9">
      <stop offset="0" stop-color="var(--green-light)"/>
      <stop offset="1" stop-color="var(--green-base)"/>
    </radialGradient>
    <linearGradient id="loaf-tone" x1="0" y1="0" x2="0" y2="1">
      <stop offset="0" stop-color="var(--loaf-light)"/>
      <stop offset="1" stop-color="var(--loaf-dark)"/>
    </linearGradient>
    <g id="pack-artwork">
      <g clip-path="url(#bag-clip)">
        <use href="#sunburst" transform="translate(150,140)"/>
      </g>
      <g role="img" aria-label="Photo of sliced buttermilk loaf seen through the pack window">
        <use href="#bread-heart" class="bread-window" fill="url(#loaf-tone)"/>
      </g>
      <ellipse class="quality-badge" cx="322" cy="46" rx="48" ry="26"/>
      <rect class="flavour-pill" x="113" y="179" width="139" height="27" rx="13.5"/>
      <text class="flavour-label" x="182.5" y="199" text-anchor="middle">BUTTER MILK</text>
    </g>
  </defs>

  <g class="pack pack--yellow" transform="translate(126,58)">
    <use href="#bag-outline" fill="url(#glow-yellow)"/>
    <use href="#pack-artwork"/>
    <text class="pack-title" x="18" y="108">GOLDEN</text>
    <text class="pack-title" x="70" y="166">HEARTH</text>
  </g>

  <g class="pack pack--red" transform="translate(126,422)">
    <use href="#bag-outline" fill="url(#glow-red)"/>
    <use href="#pack-artwork"/>
    <text class="pack-title" x="18" y="108">GOLDEN</text>
    <text class="pack-title" x="70" y="166">HEARTH</text>
  </g>

  <g class="pack pack--green" transform="translate(126,868)">
    <use href="#bag-outline" fill="url(#glow-green)"/>
    <use href="#pack-artwork"/>
    <text class="pack-title" x="18" y="108">GOLDEN</text>
    <text class="pack-title" x="70" y="166">HEARTH</text>
  </g>
</svg>
</body>
</html>
```